Harlow Brickwell Ltd- building and maintenance company looking to create professional branding for m

creation of a website for a building and maintenance company,
will need a gallery and references/ reviews page
homepage to have some company information with rolling photos of completed works
all suggestions welcome on additional requirements for website.
layout should be easy to navigate.

Target Market(s)

30-70s homeowners with mid to high income

Logo Text

Harlow Brickwell Ltd

Coding

Coded - Design and coding required

Number of Pages Required

4 page

```html
<!DOCTYPE html>
<html lang="en">
<head>
<meta charset="utf-8">
<title>Harlow Brickwell Ltd — Building and Maintenance</title>
<link href="https://fonts.googleapis.com/css2?family=Poppins:wght@400;500;600;700&display=swap" rel="stylesheet">
<style>
:root{
  --orange:#ffaa00;
  --ink:#111111;
  --muted:#555555;
  --white:#ffffff;
  --grey-band:#5f6064;
  --footer:#000000;
}
*{margin:0;padding:0;box-sizing:border-box}
html,body{width:1200px;height:3158px;overflow:hidden;background:var(--white)}
body{font-family:'Poppins',sans-serif;color:var(--ink);position:relative}
.page{position:absolute;left:176px;top:142px;width:849px;height:2876px;background:var(--white);overflow:hidden}
section,header,footer{position:absolute;left:0;width:849px}
.abs{position:absolute}
.accent{color:var(--orange)}
.btn{position:absolute;background:var(--orange);color:var(--white);font-weight:600;font-size:9px;display:flex;align-items:center;justify-content:center;letter-spacing:.3px;text-transform:uppercase}
.section-title{position:absolute;left:0;width:849px;text-align:center;font-weight:700;font-size:22px;text-transform:uppercase}
.section-title .accent{border-bottom:2px solid var(--orange);padding-bottom:1px}

/* nav */
.site-nav{top:0;height:40px;background:var(--orange)}
.brand{position:absolute;left:31px;top:11px;font-weight:700;font-size:13px;color:var(--ink);display:flex;align-items:center;gap:6px}
.brand-mark{width:10px;height:10px;background:var(--ink)}
.nav-link{position:absolute;top:15px;font-size:8px;color:var(--white);font-weight:500;text-transform:uppercase}

/* hero */
.hero{top:40px;height:389px}
.hero-photo{position:absolute;inset:0;background:linear-gradient(100deg,#2d2a26 0%,#4a3f32 40%,#7a5e36 70%,#3d3630 100%)}
.hero-title{position:absolute;left:32px;top:117px;color:var(--white);font-weight:700;font-size:28px;line-height:43px;text-transform:uppercase}
.hero-text{position:absolute;left:33px;top:203px;width:390px;color:#e8e8e8;font-size:10.5px;line-height:16px}

/* services */
.services{top:429px;height:372px}
.view-more{position:absolute;font-size:9px;font-weight:500}
.service-card{position:absolute;top:113px;width:157px;height:214px;background:var(--white);box-shadow:0 2px 8px rgba(0,0,0,.22);text-align:center}
.service-photo{position:absolute;left:39px;top:15px;width:78px;height:78px;border-radius:50%}
.service-name{position:absolute;left:0;width:157px;top:105px;color:var(--orange);font-size:13px;font-weight:500;text-transform:uppercase}
.service-text{position:absolute;left:12px;width:133px;top:128px;font-size:8px;line-height:12.3px;color:#444}
.service-card .btn{left:49px;top:180px;width:59px;height:13px;font-size:6.5px;font-weight:500}
.carousel-arrow{position:absolute;top:211px}

/* cost banner */
.cost-banner{top:801px;height:261px}
.cost-photo{position:absolute;inset:0;background:linear-gradient(90deg,#595a5e 0%,#5f6064 45%,#6a5f54 65%,#7d6c5a 85%,#5f5c58 100%)}
.cost-title{position:absolute;left:38px;top:50px;color:var(--white);font-weight:600;font-size:22px;line-height:28px}
.cost-text{position:absolute;left:37px;top:115px;width:275px;color:#eeeeee;font-size:10.5px;line-height:16px}

/* about */
.about{top:1062px;height:317px}
.about-title{position:absolute;left:58px;top:64px;font-weight:700;font-size:29px;line-height:43px;text-transform:uppercase}
.about-text{position:absolute;left:58px;top:157px;width:335px;font-size:10.8px;line-height:16px;color:#222}
.about-photo{position:absolute;left:443px;top:62px;width:361px;height:220px;background:linear-gradient(120deg,#3a4048,#6d7480 50%,#2f353c)}

/* projects */
.projects{top:1379px;height:350px}
.tile{position:absolute}

/* team */
.team{top:1729px;height:362px}
.team-intro{position:absolute;left:0;width:849px;top:86px;text-align:center;font-size:10.5px;line-height:16px;color:#222}
.member{position:absolute;top:139px;width:200px;text-align:center}
.member-photo{width:96px;height:96px;border-radius:50%;margin:0 auto;background:linear-gradient(180deg,#f1c24a 0%,#f1c24a 28%,#e7ebf0 28%,#d0d6de 100%)}
.member-name{margin-top:23px;color:var(--orange);font-size:11px;font-weight:500;letter-spacing:1px;text-transform:uppercase}
.member-role{margin-top:1px;font-size:6.5px;color:#333;text-transform:uppercase}
.member-phone{margin-top:3px;color:var(--orange);font-size:11px}
.member-mail{margin-top:2px;font-size:6.5px;color:#333;text-transform:uppercase}

/* work with */
.work-with{top:2091px;height:260px}
.work-photo{position:absolute;inset:0;background:linear-gradient(90deg,#3c4350 0%,#5d6068 40%,#8a7c74 55%,#5e616a 75%,#3f4552 100%)}
.work-title{position:absolute;left:0;width:849px;top:46px;text-align:center;color:var(--white);font-weight:700;font-size:21px;text-transform:uppercase}
.work-text{position:absolute;left:134px;top:106px;width:585px;color:#eeeeee;font-size:10.5px;line-height:16px}

/* feedback */
.feedback{top:2351px;height:363px}
.feedback-box{position:absolute;left:38px;top:90px;width:415px;height:123px;background:var(--orange)}
.feedback-lead{position:absolute;left:66px;top:24px;width:200px;color:var(--white);font-weight:700;font-size:24px;line-height:37px;white-space:nowrap}
.round-arrow{position:absolute;top:246px;width:28px;height:28px;border-radius:50%;background:var(--orange)}
.review-card{position:absolute;left:315px;top:129px;width:454px;height:177px;background:var(--white);box-shadow:0 2px 10px rgba(0,0,0,.14)}
.review-avatar{position:absolute;left:198px;top:-29px;width:58px;height:58px;border-radius:50%;border:2px solid var(--white);background:linear-gradient(180deg,#b9b2aa,#e5e1dc)}
.review-quote{position:absolute;color:var(--orange);font-size:16px;font-weight:700;line-height:1}
.review-text{position:absolute;left:10px;width:434px;top:75px;text-align:center;font-size:9px;line-height:14px;color:#222}
.review-name{position:absolute;right:38px;top:130px;font-size:9px;font-weight:700}

/* footer */
.site-footer{top:2714px;height:162px;background:var(--footer);color:var(--white)}
.footer-brand{position:absolute;left:80px;top:38px;font-weight:700;font-size:16px}
.footer-blurb{position:absolute;left:80px;top:64px;width:170px;font-size:5.6px;line-height:7.6px;color:#dddddd}
.footer-head{position:absolute;top:41px;font-size:8px;text-transform:uppercase}
.footer-list{position:absolute;font-size:7px;line-height:12px;color:#dddddd;list-style:none}
.footer-small{position:absolute;font-size:6.5px;line-height:11px;color:#dddddd}
.social{position:absolute;left:728px;top:59px;display:flex;gap:3px}
.social span{width:6px;height:6px;border-radius:50%;background:var(--white)}
.footer-rule{position:absolute;left:0;top:130px;width:849px;height:1px;background:#333}
.copyright{position:absolute;left:0;width:849px;top:143px;text-align:center;font-size:7px;letter-spacing:.5px;color:#dddddd}
</style>
</head>
<body>
<div class="page">

  <header class="site-nav">
    <div class="brand"><span class="brand-mark"></span>HARLOW BRICKWELL LTD</div>
    <span class="nav-link" style="left:380px">Home</span>
    <span class="nav-link" style="left:455px">Service</span>
    <span class="nav-link" style="left:542px">Projects</span>
    <span class="nav-link" style="left:638px">About us</span>
    <span class="nav-link" style="left:734px">Contact us</span>
  </header>

  <section class="hero">
    <div class="hero-photo" role="img" aria-label="Photo of a construction worker in a yellow hard hat and safety glasses inside a workshop"></div>
    <h1 class="hero-title">Building <span class="accent">and</span> Maintenance<br>Company</h1>
    <p class="hero-text">whether you require a one off service or require multiple service contracts, we can provide the solution for you.</p>
    <div class="btn" style="left:34px;top:246px;width:104px;height:24px">Contact us</div>
  </section>

  <section class="services">
    <h2 class="section-title" style="top:34px">Services <span class="accent">we offer</span></h2>
    <span class="view-more" style="left:697px;top:86px">View More</span>
    <svg class="abs" style="left:756px;top:89px" width="6" height="8" viewBox="0 0 6 8"><path d="M1 1l3 3-3 3" fill="none" stroke="#111" stroke-width="1.3"/></svg>

    <svg class="carousel-arrow" style="left:40px" width="10" height="16" viewBox="0 0 10 16"><path d="M8 2L2 8l6 6" fill="none" stroke="#111" stroke-width="1.8"/></svg>
    <svg class="carousel-arrow" style="left:789px" width="10" height="16" viewBox="0 0 10 16"><path d="M2 2l6 6-6 6" fill="none" stroke="#111" stroke-width="1.8"/></svg>

    <article class="service-card" style="left:77px">
      <div class="service-photo" role="img" aria-label="Photo of an electrical fuse board" style="background:linear-gradient(160deg,#8a8f96,#d8dadd 50%,#5a5f66)"></div>
      <h3 class="service-name">Electrical</h3>
      <p class="service-text">we are specialists in all aspects of domestic and commercial plumbing, heating and boiler services.</p>
      <div class="btn">Read more</div>
    </article>
    <article class="service-card" style="left:253px">
      <div class="service-photo" role="img" aria-label="Photo of a plumber fitting a pipe" style="background:linear-gradient(160deg,#7a5b3a,#c9a77a 50%,#4f3a25)"></div>
      <h3 class="service-name">Plumbing</h3>
      <p class="service-text">we are specialists in all aspects of domestic and commercial plumbing, heating and boiler services .</p>
      <div class="btn">Read more</div>
    </article>
    <article class="service-card" style="left:428px">
      <div class="service-photo" role="img" aria-label="Photo of an electrical fuse board" style="background:linear-gradient(160deg,#8a8f96,#d8dadd 50%,#5a5f66)"></div>
      <h3 class="service-name">Electrical</h3>
      <p class="service-text">we are specialists in all aspects of domestic and commercial plumbing, heating and boiler services.</p>
      <div class="btn">Read more</div>
    </article>
    <article class="service-card" style="left:604px">
      <div class="service-photo" role="img" aria-label="Photo of a worker repairing a ceiling" style="background:linear-gradient(160deg,#5a4c44,#e0dcd8 55%,#a33a3a)"></div>
      <h3 class="service-name">Flooring</h3>
      <p class="service-text">we are specialists in all aspects of domestic and commercial plumbing, heating and boiler services.</p>
      <div class="btn">Read more</div>
    </article>
  </section>

  <section class="cost-banner">
    <div class="cost-photo" role="img" aria-label="Photo of two smiling maintenance workers in work uniforms"></div>
    <h2 class="cost-title">Looking for <span class="accent">cost effective</span><br>Maintenance services?</h2>
    <p class="cost-text">we provide reactive building and property maintenance services across the whole of the city. all our tradesmen are fully qualified, very experienced and have years of know how.</p>
    <div class="btn" style="left:37px;top:194px;width:107px;height:23px">Contact us</div>
  </section>

  <section class="about">
    <h2 class="about-title">About <span class="accent">Harlow</span><br><span class="accent">Brickwell</span></h2>
    <p class="about-text">lorem ipsum dolor sit amet, consectetur adipiscing elit. lorem tellus justo, imperdiet eu id laoreet eu amet, et. cursus faucibus enim et dolor lorem neque. libero orci nec aenean risus, fringilla. purus convallis vitae erat ac aliquam senectus pellentesque sagittis.</p>
    <div class="btn" style="left:58px;top:260px;width:94px;height:22px;font-weight:500">Read more</div>
    <div class="about-photo" role="img" aria-label="Photo of a smiling engineer in an orange hard hat and overalls in a factory"></div>
  </section>

  <section class="projects">
    <h2 class="section-title" style="top:20px">Total <span class="accent">projects</span></h2>
    <span class="view-more" style="left:773px;top:45px;font-size:8.5px">View All</span>
    <svg class="abs" style="left:813px;top:48px" width="5" height="7" viewBox="0 0 5 7"><path d="M1 1l2.5 2.5L1 6" fill="none" stroke="#111" stroke-width="1.1"/></svg>

    <div class="tile" role="img" aria-label="Photo of a worker in a mask cleaning a ventilation duct" style="left:25px;top:74px;width:308px;height:271px;background:linear-gradient(130deg,#d9d9d7,#9c9ea2 50%,#2a2c30)"></div>
    <div class="tile" role="img" aria-label="Photo of an electrician working on a control panel" style="left:339px;top:74px;width:230px;height:140px;background:linear-gradient(130deg,#6b7178,#3b4047 60%,#22262b)"></div>
    <div class="tile" role="img" aria-label="Photo of a hand testing a fuse board with a screwdriver" style="left:576px;top:74px;width:247px;height:140px;background:linear-gradient(130deg,#bfc2c6,#e9e9ea 55%,#c8a98a)"></div>
    <div class="tile" role="img" aria-label="Photo of a roofer working on a blue metal roof" style="left:341px;top:222px;width:230px;height:123px;background:linear-gradient(180deg,#9fb6cc 0%,#b9cad9 40%,#2d5b73 60%,#1c3f54 100%)"></div>
    <div class="tile" role="img" aria-label="Photo of a worker repairing a damaged ceiling" style="left:577px;top:222px;width:246px;height:123px;background:linear-gradient(130deg,#4e463f,#e4e1dd 50%,#4a5e88)"></div>
  </section>

  <section class="team">
    <h2 class="section-title" style="top:27px">Professional <span class="accent" style="border:0">team</span></h2>
    <p class="team-intro">lorem ipsum dolor sit amet, consectetur adipisicing elit, sed do eiusmod<br>tempor incididunt ut labore et dolore magna aliqua. ut enim ad min.</p>

    <div class="member" style="left:116px">
      <div class="member-photo" role="img" aria-label="Portrait photo of a team member in a yellow hard hat"></div>
      <div class="member-name">Owen Marsh</div>
      <div class="member-role">Lifts maintainers</div>
      <div class="member-phone">+44 (0)1632 960418</div>
      <div class="member-mail">team@harlowbrickwell.tld</div>
    </div>
    <div class="member" style="left:316px">
      <div class="member-photo" role="img" aria-label="Portrait photo of a team member in a yellow hard hat"></div>
      <div class="member-name">Dana Whitlow</div>
      <div class="member-role">Fire alarm maintainers</div>
      <div class="member-phone">+44 (0)1632 960418</div>
      <div class="member-mail">team@harlowbrickwell.tld</div>
    </div>
    <div class="member" style="left:526px">
      <div class="member-photo" role="img" aria-label="Portrait photo of a team member in a yellow hard hat"></div>
      <div class="member-name">Claire Ashby</div>
      <div class="member-role">Light protection maintainers</div>
      <div class="member-phone">+44 (0)1632 960418</div>
      <div class="member-mail">team@harlowbrickwell.tld</div>
    </div>
  </section>

  <section class="work-with">
    <div class="work-photo" role="img" aria-label="Photo of two business people shaking hands"></div>
    <h2 class="work-title">Work with <span class="accent">Harlow Brickwell</span></h2>
    <p class="work-text">looking for reliable, high quality and cost effective building maintenance and/or property repair services in the city? harlow brickwell provide a wide range of maintenance and repair services to a variety of customers including domestic users, public sector entities and businesses across the city.</p>
    <div class="btn" style="left:372px;top:173px;width:106px;height:22px">Make enquiry</div>
  </section>

  <section class="feedback">
    <h2 class="section-title" style="top:44px">Feed<span class="accent" style="border:0">back</span></h2>
    <div class="feedback-box">
      <p class="feedback-lead">What our clients<br>have to say</p>
    </div>
    <div class="round-arrow" style="left:183px">
      <svg width="28" height="28" viewBox="0 0 28 28"><path d="M18 14h-8M13 10.5L9.5 14l3.5 3.5" fill="none" stroke="#fff" stroke-width="1.8"/></svg>
    </div>
    <div class="round-arrow" style="left:227px">
      <svg width="28" height="28" viewBox="0 0 28 28"><path d="M10 14h8M15 10.5l3.5 3.5-3.5 3.5" fill="none" stroke="#fff" stroke-width="1.8"/></svg>
    </div>
    <div class="review-card">
      <div class="review-avatar" role="img" aria-label="Portrait photo of the reviewer"></div>
      <span class="review-quote" style="left:52px;top:52px">&ldquo;</span>
      <p class="review-text">I manage several rental homes and have used this team for repairs for two years now.<br>The tradesmen are punctual, tidy and helpful. I plan to keep using them for a long time!</p>
      <span class="review-quote" style="left:408px;top:110px">&rdquo;</span>
      <span class="review-name">- Mirela</span>
    </div>
  </section>

  <footer class="site-footer">
    <div class="footer-brand">Harlow Brickwell</div>
    <p class="footer-blurb">the work of the company covers planned and reactive repairs, building upkeep and small works for homeowners, landlords and local businesses across the region, all handled by our own trades.</p>

    <div class="footer-head" style="left:297px">Quick links</div>
    <ul class="footer-list" style="left:297px;top:57px">
      <li>home</li><li>service</li><li>projects</li><li>about us</li>
    </ul>

    <div class="footer-head" style="left:422px">Address</div>
    <svg class="abs" style="left:410px;top:61px" width="8" height="11" viewBox="0 0 8 11"><path d="M4 10.5S.6 6.6.6 4.2a3.4 3.4 0 016.8 0C7.4 6.6 4 10.5 4 10.5z" fill="none" stroke="#fff" stroke-width=".9"/><circle cx="4" cy="4.2" r="1.2" fill="none" stroke="#fff" stroke-width=".8"/></svg>
    <p class="footer-small" style="left:422px;top:56px">unit 12, mill lane<br>harlow</p>

    <div class="footer-head" style="left:556px">Contact us</div>
    <svg class="abs" style="left:543px;top:59px" width="9" height="7" viewBox="0 0 9 7"><rect x=".5" y=".5" width="8" height="6" fill="none" stroke="#fff" stroke-width=".8"/><path d="M.5 .8L4.5 4l4-3.2" fill="none" stroke="#fff" stroke-width=".8"/></svg>
    <p class="footer-small" style="left:556px;top:56px">hello@harlowbrickwell.tld</p>
    <svg class="abs" style="left:544px;top:72px" width="7" height="8" viewBox="0 0 7 8"><path d="M1.5.5l1.4 1.6-.8 1.1a5 5 0 002.2 2.3l1.1-.8 1.2 1.5-1 1.1C3 7 .4 4 .4 1.5z" fill="#fff"/></svg>
    <p class="footer-small" style="left:556px;top:70px">01632 960 000</p>

    <div class="footer-head" style="left:728px">Follow us</div>
    <div class="social" aria-label="Social media links"><span></span><span></span><span></span><span></span></div>

    <div class="footer-rule"></div>
    <p class="copyright">copyright © harlow brickwell 2021 all rights reserved</p>
  </footer>

</div>
</body>
</html>
```